Letterhead for New Orthopaedic Surgery Practice

My husband and I are starting our own practice named RB Spine & Vitality Center. We would like to create a nice simple but high class letterhead that doesn't use too much solid color ink when printing. I like the colors dark blue, gold, yellow. Open to other suggestions. We will need to list him and I both on the top of the letterhead. Here is the important information:
Lucinda Perrow, M.D. - Hand and Upper Extremity Surgery
Abena Quist, M.D. - Hip & Knee Replacement/General Orthopaedic Surgery
Location: 18735 North Harlow Pkwy
Ridgefield Bay, FL 33480
Phone: 954-218-4650
Fax: 954-582-1346
Email: info@myrbspine.com

The only thing is that the phone and fax numbers will change once we get into our space. I just want to get the design started. I am including several documents which are my previous practice letterhead, my current procedure room letterhead, and our new Logo. The other letterheads are just for examples but please think outside of the box! We would love to see some great designs.

Colors
0054AA
0677BA
7BADD7
CADEEF
E8F1F8
0094D4
00A9DD
6FCCEA
C7EBF8
E9F6FB

Requirements
Must have
• class, elegance, luxury

```html
<!DOCTYPE html>
<html lang="en">
<head>
<meta charset="utf-8">
<title>RB Spine &amp; Vitality Center – Letterhead</title>
<link href="https://fonts.googleapis.com/css2?family=Inter:wght@400&family=Questrial&display=swap" rel="stylesheet">
<style>
  :root {
    --page-bg: #ececec;
    --paper: #ffffff;
    --brand-blue: #0626a8;
    --brand-gold: #f8c575;
    --ink-white: #ffffff;
  }
  html, body {
    margin: 0;
    padding: 0;
    width: 977px;
    height: 1200px;
    overflow: hidden;
    background: var(--page-bg);
  }
  .letterhead {
    position: absolute;
    left: 68px;
    top: 6px;
    width: 840px;
    height: 1188px;
    background: var(--paper);
    box-shadow: 0 4px 18px rgba(0,0,0,0.25);
  }
  .letterhead svg { display: block; width: 100%; height: 100%; }
  .txt { font-family: "Questrial", sans-serif; }
  .doctor-name { fill: var(--brand-blue); font-size: 52px; }
  .doctor-degree { font-size: 34px; }
  .specialty { fill: var(--brand-blue); font-size: 31px; }
  .brand-name { fill: var(--brand-blue); font-size: 40px; text-anchor: middle; }
  .contact { font-family: "Inter", sans-serif; fill: var(--ink-white); font-size: 21px; }
  .band-gold { fill: var(--brand-gold); }
  .band-blue { fill: var(--brand-blue); }
  .icon { fill: none; stroke: var(--ink-white); stroke-width: 2; }
  .icon-solid { fill: var(--ink-white); }
</style>
</head>
<body>
<div class="letterhead">
  <svg viewBox="0 0 1266 1790" xmlns="http://www.w3.org/2000/svg">
    <!-- header bands -->
    <path class="band-gold" d="M0 0 H1266 V307 H1040 C930 307 850 272 810 212 C772 150 760 90 620 90 H0 Z"/>
    <path class="band-blue" d="M0 90 H568 L545 118 C535 130 520 136 505 136 H0 Z"/>

    <!-- practice name -->
    <text class="txt brand-name" x="1038" y="180">RB Spine &amp; Vitality</text>
    <text class="txt brand-name" x="1038" y="226">Center</text>

    <!-- physicians -->
    <text class="txt doctor-name" x="85" y="262">Lucinda Perrow, <tspan class="doctor-degree">M.D.</tspan></text>
    <text class="txt specialty" x="85" y="300">Hand and Upper Extremity Surgery</text>

    <text class="txt doctor-name" x="83" y="390">Abena Quist, <tspan class="doctor-degree">M.D.</tspan></text>
    <text class="txt specialty" x="85" y="432">Hip &amp; Knee Replacement</text>
    <text class="txt specialty" x="85" y="466">General Orthopaedic Surgery</text>

    <!-- footer band -->
    <path class="band-blue" d="M0 1641 H640 C730 1641 780 1680 820 1720 C845 1745 870 1757 900 1757 H1266 V1790 H0 Z"/>

    <!-- phone -->
    <path class="icon-solid" d="M47 1673 c3-3 6-3 8 0 l5 7 c2 3 1 5-1 7 l-3 2 c3 6 7 10 13 13 l2-3 c2-2 4-3 7-1 l7 5 c3 2 3 5 0 7 l-3 3 c-17 2-36-18-37-36 z"/>
    <text class="txt contact" x="98" y="1696">954-218-4650</text>

    <!-- fax -->
    <g class="icon">
      <rect x="52" y="1723" width="20" height="9" rx="2"/>
      <rect x="45" y="1731" width="34" height="17" rx="3"/>
      <rect x="52" y="1740" width="20" height="17"/>
      <line x1="56" y1="1746" x2="68" y2="1746"/>
      <line x1="56" y1="1751" x2="68" y2="1751"/>
    </g>
    <text class="txt contact" x="99" y="1749">954-582-1346</text>

    <!-- email -->
    <g class="icon">
      <rect x="275" y="1671" width="32" height="21"/>
      <polyline points="275,1671 291,1684 307,1671"/>
      <line x1="275" y1="1692" x2="287" y2="1681"/>
      <line x1="307" y1="1692" x2="295" y2="1681"/>
    </g>
    <text class="txt contact" x="323" y="1689">info@myrbspine.com</text>

    <!-- location -->
    <path class="icon-solid" fill-rule="evenodd" d="M286 1760 C279 1748 275 1740 275 1733 a11 11 0 0 1 22 0 c0 7-4 15-11 27 z M286 1728 a4.5 4.5 0 1 0 0.01 0 z"/>
    <text class="txt contact" x="323" y="1749">18735 North Harlow Pkwy, Ridgefield Bay, FL 33480</text>
  </svg>
</div>
</body>
</html>
```